TITLE: What Makes My Child’s Playing Talent Grow? SUB-TITLE: A Mother’s Plain Talk Manual for Coaching...

My book is for parents who have young children that are really into sports. My book empowers parents so they can motivate their children to succeed. It deals with sports psychology. Both my title and subtitle should be easy to read. Ideally, I would like a picture of young athlete(s) on the title. I have uploaded files of some books on Brindlemart that deal with the same subject. The last two files are 1) my company logo, please try to include these colors 2) an ebook cover I put together myself. You will notice an On-line bonus in the middle of the book, this Bonus needs to be on the cover.

Target Market(s)

Parents with children who play sports at a high level

Colors

Designer to choose colors to be used in the design.

Requirements
Must have
• Online Bonus feature as per my example.
• Dimensions: Pagelux = The ideal size of your eBook cover art is a height/width ratio of 1.6:1. This means that for every 1,000 pixels in width, the image should be 1,600 pixels in height.
Nice to have
• picture of a young athlete or young athletes

```html
<!DOCTYPE html>
<html lang="en">
<head>
<meta charset="utf-8">
<title>What Makes My Child’s Playing Talent Grow? — Cover</title>
<link href="https://fonts.googleapis.com/css2?family=Oswald:wght@400;600;700&display=swap" rel="stylesheet">
<style>
  :root {
    --page-bg: #e9e9e9;
    --cover-deep: #1e0c26;
    --cover-plum: #4a1f55;
    --cover-glow: #7a3f7f;
    --title-orange: #f39a1e;
    --title-white: #ffffff;
    --sub-white: #f2ecf4;
    --author-orange: #f0a02a;
    --badge-orange: #f28c1c;
    --badge-ring: #ffffff;
  }
  * { box-sizing: border-box; margin: 0; padding: 0; }
  html, body {
    width: 1200px; height: 706px; overflow: hidden;
    background: var(--page-bg);
  }
  .stage {
    position: relative; width: 1200px; height: 706px;
  }
  .cover {
    position: absolute; left: 400px; top: 62px;
    width: 400px; height: 582px;
    overflow: hidden;
    background: radial-gradient(ellipse at 50% 55%, var(--cover-glow) 0%, var(--cover-plum) 40%, var(--cover-deep) 100%);
    font-family: "Oswald", "Arial Narrow", sans-serif;
    text-align: center;
    color: var(--title-white);
  }
  .cover-photo {
    position: absolute; left: 90px; top: 250px; width: 220px; height: 200px;
    background: radial-gradient(ellipse at 50% 55%, rgba(240,140,60,0.35) 0%, rgba(70,110,200,0.25) 45%, rgba(30,12,38,0) 75%);
  }
  .publisher-mark {
    position: absolute; left: 10px; top: 8px;
    width: 36px; height: 36px; border-radius: 50%;
    background: var(--badge-orange);
    border: 3px solid var(--badge-ring);
  }
  .bonus-badge {
    position: absolute; left: 330px; top: 38px;
    width: 54px; height: 54px; border-radius: 50%;
    background: var(--badge-orange);
    border: 2px solid var(--badge-ring);
    display: flex; flex-direction: column; align-items: center; justify-content: center;
    line-height: 1.05; font-weight: 700; font-size: 7px; color: var(--title-white);
  }
  .bonus-badge .bonus-note { font-weight: 400; font-size: 5px; margin-top: 2px; }
  .title {
    position: absolute; left: 0; right: 0; top: 40px;
    text-transform: uppercase; line-height: 1;
  }
  .title .line-small {
    display: block; font-weight: 600; font-size: 30px; letter-spacing: 1px;
    color: var(--title-white);
  }
  .title .line-big {
    display: block; font-weight: 700; font-size: 56px; letter-spacing: 1px;
    color: var(--title-orange); margin: 2px 0 4px;
  }
  .subtitle {
    position: absolute; left: 40px; right: 40px; top: 462px;
    font-weight: 400; font-size: 15px; line-height: 1.3; letter-spacing: 0.5px;
    text-transform: uppercase; color: var(--sub-white);
  }
  .author {
    position: absolute; left: 0; right: 0; top: 530px;
    font-weight: 600; font-size: 24px; letter-spacing: 1.5px;
    text-transform: uppercase; color: var(--author-orange);
  }
</style>
</head>
<body>
  <main class="stage">
    <section class="cover">
      <div class="cover-photo" role="img" aria-label="Photo of a young athlete's legs and running shoes sprinting through purple haze"></div>
      <div class="publisher-mark" aria-hidden="true"></div>
      <div class="bonus-badge">
        <span>FREE</span><span>ONLINE</span><span>WORKBOOK</span>
        <span class="bonus-note">BONUS INSIDE</span>
      </div>
      <h1 class="title">
        <span class="line-small">What Makes My</span>
        <span class="line-big">Child’s</span>
        <span class="line-small">Playing</span>
        <span class="line-big">Talent</span>
        <span class="line-small">Grow?</span>
      </h1>
      <p class="subtitle">A Mother’s Plain Talk Manual for Coaching Confident, Focused and Resilient Athletes</p>
      <p class="author">Lena Marchetti</p>
    </section>
  </main>
</body>
</html>
```